Business Card/Logo Design Project

Design the Business card For a psychologist providing relationship workshops, see website draft at www.brightmorrowtalks.com.au.

The background is to be beige with shadows in ivory of the letter "L" as shown on the website noted above.

The words "Kindred Hours" on the front with the first letter of each word in very scrolled lettering and the remaining letters more formal. The front design is to be the logo of the business for use on other items.

The reverse is to show...

client's name
date
time
workshop number
workshop name
and at the bottom "PLEASE BE PUNCTUAL. BRING NOTEPAD & PEN"

Target Market(s)

female, middle-class, educated, introspective

Industry/Entity Type

Business

Requirements
Must have
• see www.brightmorrowtalks.com.au for the design aesthetic - just need you to make it look professional.

cream, beige, grey, chocolate, tan, ivory.

calligraphy shadows as per referenced website

business card back, flyer and postcard to just be background so that I can add text on top through papercrane.

see website for colour-scheme.
Should not have
• not cutesy, pink, or mushy

```html
<!DOCTYPE html>
<html lang="en">
<head>
<meta charset="utf-8">
<title>Kindred Hours – Business Card</title>
<link href="https://fonts.googleapis.com/css2?family=EB+Garamond:wght@400;500&display=swap" rel="stylesheet">
<style>
  :root {
    --backdrop: #eeeeee;
    --cream-light: #fbf6e4;
    --cream: #f3e8c6;
    --beige: #e6d4a2;
    --chocolate: #8a5e42;
    --ink-brown: #7a5036;
    --ivory-text: #f6edd2;
    --ivory-shadow: rgba(255, 250, 228, 0.55);
    --band-shadow: rgba(214, 180, 140, 0.28);
    --rule: #8a6a52;
  }
  * { box-sizing: border-box; margin: 0; padding: 0; }
  html, body {
    width: 1200px; height: 522px; overflow: hidden;
    background: var(--backdrop);
  }
  body { position: relative; font-family: "EB Garamond", Georgia, serif; color: var(--ink-brown); }

  .card {
    position: absolute; top: 104px;
    width: 531px; height: 295px;
    overflow: hidden;
    box-shadow: 0 10px 18px rgba(0,0,0,0.18);
  }

  /* Front */
  .card--front {
    left: 52px;
    background: radial-gradient(ellipse at 62% 20%, var(--cream-light) 0%, var(--cream) 45%, var(--beige) 100%);
  }
  .front-shadow {
    position: absolute; left: 60px; top: 30px;
    width: 220px; height: 190px;
    background: radial-gradient(ellipse at 50% 50%, var(--ivory-shadow) 0%, rgba(255,250,228,0) 70%);
  }
  .front-band {
    position: absolute; left: 0; right: 0; top: 127px; bottom: 0;
    background: var(--chocolate);
  }
  .band-shadow {
    position: absolute; left: 260px; top: 180px;
    width: 240px; height: 80px;
    background: radial-gradient(ellipse at 50% 50%, var(--band-shadow) 0%, rgba(214,180,140,0) 70%);
  }
  .brand-name {
    position: absolute; left: 0; right: 0; top: 142px;
    text-align: center; line-height: 1;
    font-size: 64px; font-weight: 400; letter-spacing: 1px;
    color: var(--ivory-text);
  }

  /* Back */
  .card--back { left: 602px; }
  .back-texture {
    position: absolute; inset: 0;
    background:
      linear-gradient(120deg, rgba(255,252,238,0) 30%, rgba(255,252,238,0.45) 38%, rgba(255,252,238,0) 46%),
      linear-gradient(60deg, rgba(255,252,238,0) 62%, rgba(255,252,238,0.4) 70%, rgba(255,252,238,0) 78%),
      radial-gradient(ellipse at 70% 15%, rgba(255,252,238,0.7) 0%, rgba(255,252,238,0) 55%),
      linear-gradient(160deg, var(--cream) 0%, var(--cream-light) 50%, var(--beige) 100%);
  }
  .field-title {
    position: absolute; top: 44px; left: 0; right: 0;
    text-align: center; font-size: 17px;
  }
  .field-row {
    position: absolute; left: 49px; right: 48px;
    display: flex; align-items: baseline;
    font-size: 19px; white-space: nowrap;
  }
  .field-line {
    flex: 1; border-bottom: 1px solid var(--rule);
    height: 1px; margin-left: 6px; transform: translateY(2px);
  }
  .field-line--short { flex: 0 0 148px; margin-right: 2px; }
  .row-client { top: 77px; }
  .row-date { top: 114px; }
  .row-workshop { top: 152px; }
  .blank-line {
    position: absolute; left: 49px; right: 48px; top: 209px;
    border-bottom: 1px solid var(--rule);
  }
  .card-note {
    position: absolute; left: 0; right: 0; top: 242px;
    text-align: center; font-size: 17px;
  }
</style>
</head>
<body>
  <section class="card card--front" aria-label="Business card front">
    <div class="front-shadow" role="img" aria-label="Faint ivory calligraphic letter shadow"></div>
    <div class="front-band"></div>
    <div class="band-shadow" role="img" aria-label="Faint tan calligraphic letter shadow on the band"></div>
    <h1 class="brand-name">Kindred Hours</h1>
  </section>

  <section class="card card--back" aria-label="Business card back">
    <div class="back-texture" role="img" aria-label="Soft beige background with faint ivory calligraphic swirls"></div>
    <p class="field-title">Appointment/Workshop</p>
    <div class="field-row row-client"><span>Client Name</span><span class="field-line"></span></div>
    <div class="field-row row-date"><span>Date(s)</span><span class="field-line field-line--short"></span><span>Time</span><span class="field-line"></span></div>
    <div class="field-row row-workshop"><span>Workshop No’ &amp; Name</span><span class="field-line"></span></div>
    <div class="blank-line"></div>
    <p class="card-note">Please be Punctual.&nbsp; Bring a Notepad &amp; Pen</p>
  </section>
</body>
</html>
```